Organic lawn care

take the same sign as the mosquito sign, only instead of the mosquito image have the red circle and line cross out the text of "chemicals". Have the sign say "this lawn receives ORGANIC grass treatments" "instantly SAFE for people and pets"

Lawn Care

```html
<!DOCTYPE html>
<html lang="en">
<head>
<meta charset="utf-8">
<title>Organic Lawn Care Sign</title>
<link rel="stylesheet" href="https://fonts.googleapis.com/css2?family=Archivo+Black&family=Arimo:wght@700&display=swap">
<style>
  :root {
    --backdrop: #000000;
    --sign-red: #f5141c;
    --sign-yellow: #e6ff12;
    --ink: #000000;
  }
  html, body {
    margin: 0;
    padding: 0;
    overflow: hidden;
    background: var(--backdrop);
  }
  .canvas {
    width: 1200px;
    height: 1166px;
    display: block;
  }
  .headline {
    font-family: "Archivo Black", "Arial Black", sans-serif;
    fill: var(--ink);
  }
  .message {
    font-family: "Arimo", Arial, sans-serif;
    font-weight: 700;
    fill: var(--ink);
  }
  .safety-box {
    fill: none;
    stroke: var(--ink);
    stroke-width: 3;
  }
  .ring { fill: var(--sign-red); }
  .face { fill: var(--sign-yellow); }
  .slash { stroke: var(--sign-red); stroke-width: 60; }
  .headline-knockout { fill: var(--sign-yellow); }
</style>
</head>
<body>
<svg class="canvas" viewBox="0 0 926 900" xmlns="http://www.w3.org/2000/svg" aria-label="No chemicals: this lawn receives organic grass treatments, instantly safe for people and pets">
  <defs>
    <clipPath id="sign-face">
      <circle cx="463" cy="450" r="384"/>
    </clipPath>
  </defs>

  <circle class="ring" cx="463" cy="450" r="443"/>
  <circle class="face" cx="463" cy="450" r="384"/>

  <line class="slash" x1="200" y1="125" x2="810" y2="670" clip-path="url(#sign-face)"/>

  <rect class="headline-knockout" x="270" y="234" width="170" height="84"/>
  <text class="headline" x="460" y="308" font-size="86" text-anchor="middle" textLength="610" lengthAdjust="spacingAndGlyphs">CHEMICALS</text>

  <text class="message" x="311" y="454" font-size="36" text-anchor="middle">This lawn receives</text>
  <text class="message" x="316" y="526" font-size="54" text-anchor="middle">ORGANIC</text>
  <text class="message" x="316" y="578" font-size="36" text-anchor="middle">grass treatments</text>

  <rect class="safety-box" x="313" y="641" width="289" height="144"/>
  <text class="message" x="458" y="685" font-size="27" text-anchor="middle">Instantly</text>
  <text class="message" x="458" y="731" text-anchor="middle"><tspan font-size="38">SAFE</tspan><tspan font-size="27"> for</tspan></text>
  <text class="message" x="458" y="763" font-size="27" text-anchor="middle">People and Pets</text>
</svg>
</body>
</html>
```